Homeowners Insurance Provider Website

We are selling homeowners insurance policy / tenants Policy/Flood Insurance in USA in few states and planning expand nationally.

Our target audience are two folds: Customers (Buy policies) and Insurance Agents who wants to work with us to sell our policies to customers. But website should focus 80% on customers and 20% on agents. So, more customer focused user experience. Please note that there is no direct buy option for customers. They always go through insurance agents.

Customer focused, educational that makes buyer journey easy. We don’t want to come off as trying sell something as there is no direct sales involved from website.

Target Market(s)

Homeowners in USA and Insurance agent who sells these insurance.

Industry/Entity Type

Insurance

Number of Pages Required

4 page

Font styles to use
Other font styles liked:
• Open to suggestions

Colors

Designer to choose colors to be used in the design.

Requirements
Must have
• Three most important things: Trustworthy, Authentic, Simple
• Please use colors form logo and grays
• We like: www.brightmeadow.com
• https://www.harborlinden.com/
• We need Agent Look up tool on home page similar to what is shown on example sites.
• Design:
• Home Page - Open to Ideas
• Insurance (Products) Landing Page - Info similar to: https://www.harborlinden.com/insurance/
• Agents Page - https://www.harborlinden.com/agents/
• Claims Page - Information similar to: https://www.harborlinden.com/claims-center/
• Site Navigation:
• Home
• Insurance
• Claims
• Agents
• About Us
• Contact Us
Nice to have
• Elegant, minimal and clean design that reflects trust and authenticity.
Should not have
• Slider or rotating images - prefer flat design. Not over powering design.

```html
<!DOCTYPE html>
<html lang="en">
<head>
<meta charset="utf-8">
<title>Hearthstead Insurance Co. — Home</title>
<link rel="stylesheet" href="https://fonts.googleapis.com/css2?family=Catamaran:wght@500;600;700&family=Lato:wght@700&family=Open+Sans:wght@400;600&display=swap">
<style>
:root{
  --navy:#1e3a78;
  --navy-deep:#1f3b7a;
  --red:#d0202e;
  --text:#5a5a5a;
  --text-dark:#4a4a4a;
  --card:#ececec;
  --hero-light:#f4f4f4;
  --hero-mid:#e4e4e4;
  --footer:#323232;
  --white:#ffffff;
}
*{margin:0;padding:0;box-sizing:border-box}
html,body{width:1200px;height:2250px;overflow:hidden;background:var(--white)}
body{font-family:"Open Sans",Arial,sans-serif;color:var(--text);position:relative}
.abs{position:absolute}

/* header */
.site-header{position:absolute;left:0;top:0;width:1200px;height:114px;background:var(--white)}
.brand{position:absolute;left:78px;top:36px;display:flex;align-items:center;gap:14px}
.brand-mark{width:40px;height:40px;border-radius:50%;background:var(--navy)}
.brand-name{font-family:"Catamaran",sans-serif;font-weight:700;font-size:26px;color:var(--navy);letter-spacing:.5px}
.main-nav{position:absolute;top:46px;right:78px;display:flex;gap:28px;font-size:17px;text-transform:uppercase}
.main-nav a{color:#555;text-decoration:none}
.main-nav a.is-active{color:var(--navy)}

/* hero */
.hero{position:absolute;left:0;top:114px;width:1200px;height:490px;background:linear-gradient(90deg,var(--hero-mid),var(--hero-light) 45%,#f2f2f2)}
.hero-photo{position:absolute;left:660px;top:0;width:540px;height:490px;background:linear-gradient(160deg,#eef0f2 0%,#c9d6e4 45%,#6f9cc4 100%)}
.hero-title{position:absolute;left:80px;top:166px;font-family:"Catamaran",sans-serif;font-weight:700;font-size:35px;color:var(--navy)}
.hero-text{position:absolute;left:80px;top:224px;width:540px;font-size:16px;line-height:27px;color:var(--text)}
.btn-agent{position:absolute;left:78px;top:298px;width:196px;height:47px;display:flex;border-radius:3px;overflow:hidden;text-decoration:none}
.btn-agent .label{flex:1;background:var(--navy);color:var(--white);font-family:"Lato",sans-serif;font-weight:700;font-size:19px;display:flex;align-items:center;padding-left:19px}
.btn-agent .arrow{width:42px;background:var(--red);display:flex;align-items:center;justify-content:center}

/* policy strip */
.policy-line{position:absolute;left:78px;top:603px;width:1044px;border-top:2px dotted var(--navy)}
.policy{position:absolute;top:572px;width:240px;text-align:center}
.policy-icon{width:64px;height:64px;margin:0 auto;border:2px solid var(--navy);border-radius:50%;background:var(--white);display:flex;align-items:center;justify-content:center}
.policy-name{margin-top:20px;font-size:19px;color:#555}

/* welcome */
.welcome-title{position:absolute;left:0;top:738px;width:1200px;text-align:center;font-family:"Catamaran",sans-serif;font-weight:700;font-size:31px;color:var(--navy)}
.accent{color:var(--red)}
.welcome-text{position:absolute;left:168px;top:789px;width:864px;text-align:center;font-size:15.5px;line-height:25px;color:var(--text)}

/* products */
.products{position:absolute;left:0;top:916px;width:1200px;height:489px;background:var(--navy-deep)}
.products-title{position:absolute;left:0;top:40px;width:1200px;text-align:center;font-family:"Catamaran",sans-serif;font-weight:600;font-size:40px;color:var(--white)}
.product{position:absolute;width:330px;color:var(--white)}
.product h3{font-family:"Lato",sans-serif;font-weight:700;font-size:22px;margin-bottom:6px}
.product p{font-size:16px;line-height:25px}
.product.is-left{text-align:right;left:82px}
.product.is-right{left:789px}
.product-icon{position:absolute;width:110px;height:110px;border-radius:50%;border:3px solid var(--red);display:flex;align-items:center;justify-content:center}
.product-icon::before{content:"";position:absolute;inset:4px;border:2px solid var(--red);border-radius:50%}
.cross-h{position:absolute;left:555px;top:274px;width:90px;border-top:1px solid rgba(255,255,255,.5)}
.cross-v{position:absolute;left:600px;top:229px;height:90px;border-left:1px solid rgba(255,255,255,.5)}

/* blog */
.blog-title{position:absolute;left:0;top:1440px;width:1200px;text-align:center;font-family:"Catamaran",sans-serif;font-weight:700;font-size:41px;color:var(--navy)}
.blog-card{position:absolute;top:1509px;width:323px;height:229px;background:var(--card);padding:0 14px}
.blog-card h4{margin-top:41px;font-family:"Lato",sans-serif;font-weight:700;font-size:23px;color:var(--text-dark)}
.blog-card p{margin-top:8px;font-size:15.5px;line-height:25px;color:var(--text)}
.blog-meta{margin-top:14px;border-top:1px solid #c9c9c9;padding-top:12px;display:flex;justify-content:space-between;font-size:15px;color:var(--text-dark)}
.blog-meta span{display:flex;align-items:center;gap:6px}

/* footer */
.site-footer{position:absolute;left:0;top:1812px;width:1200px;height:438px;background:var(--footer);color:var(--white)}
.footer-tabs{position:absolute;left:308px;top:42px;width:586px;font-size:19px}
.footer-tabs span{position:absolute;top:0}
.tab-rule{position:absolute;top:86px;height:3px}
.contact-ring{position:absolute;top:148px;width:120px;height:120px;border-radius:50%;background:var(--white);border:9px solid #8a8a8a;display:flex;align-items:center;justify-content:center}
.contact-dots{position:absolute;top:207px;width:125px;border-top:2px dotted #6a6a6a}
.contact-text{position:absolute;top:294px;text-align:center;font-size:15.5px;line-height:25px}
.copyright{position:absolute;left:0;top:386px;width:1200px;text-align:center;font-size:15.5px}
</style>
</head>
<body>

<header class="site-header">
  <div class="brand"><span class="brand-mark"></span><span class="brand-name">Hearthstead Insurance Co.</span></div>
  <nav class="main-nav">
    <a class="is-active" href="#">Home</a><a href="#">About</a><a href="#">Insurance</a><a href="#">Claims</a><a href="#">Agents</a><a href="#">Contact</a>
  </nav>
</header>

<section class="hero">
  <div class="hero-photo" role="img" aria-label="Photo of a smiling family of four at the doorway of their home"></div>
  <h1 class="hero-title">Find Your Insurance Agent Now!</h1>
  <p class="hero-text">Lorem Ipsum is simply dummy text of the printing and typesetting industry. Lorem Ipsum has been the industry's standard.</p>
  <a class="btn-agent" href="#"><span class="label">FIND AGENT</span><span class="arrow">
    <svg width="20" height="18" viewBox="0 0 20 18" fill="none" stroke="#fff" stroke-width="2.4"><path d="M2 2l7 7-7 7M10 2l7 7-7 7"/></svg></span></a>
</section>

<div class="policy-line"></div>
<div class="policy" style="left:211px">
  <div class="policy-icon"><svg width="34" height="30" viewBox="0 0 34 30" fill="var(--red)"><path d="M17 3L5 13h4v8h16v-8h4z"/><path d="M2 18c4 0 7 3 9 8H6zM32 18c-4 0-7 3-9 8h5z"/></svg></div>
  <div class="policy-name">homeowners insurance</div>
</div>
<div class="policy" style="left:480px">
  <div class="policy-icon"><svg width="34" height="30" viewBox="0 0 34 30" fill="none" stroke="var(--red)" stroke-width="2.6"><path d="M5 14L17 4l12 10M9 12v10h16V12"/><path d="M6 24c5 4 17 4 22 0"/></svg></div>
  <div class="policy-name">Tenants Policy</div>
</div>
<div class="policy" style="left:748px">
  <div class="policy-icon"><svg width="34" height="30" viewBox="0 0 34 30" fill="none" stroke="var(--red)" stroke-width="2.4"><path d="M6 12L17 4l11 8M9 11v9h16v-9"/><rect x="14" y="13" width="6" height="5"/><path d="M4 24q3-3 6 0t6 0 6 0 6 0 4 0"/></svg></div>
  <div class="policy-name">Flood Insurance</div>
</div>

<h2 class="welcome-title">Welcome <span class="accent">Visitors!</span></h2>
<p class="welcome-text">Lorem Ipsum is simply dummy text of the printing and typesetting industry. Lorem Ipsum has been the industry's standard dummy text ever since the 1500s, when an unknown printer took a galley of type and scrambled it to make a type specimen book. It has survived not only five centuries, but also the leap into electronic typesetting.</p>

<section class="products">
  <h2 class="products-title">Our Products</h2>
  <div class="cross-h"></div><div class="cross-v"></div>

  <div class="product is-left" style="top:128px"><h3>Homeowners</h3><p>Lorem ipsum dolor sit amet, consectetur adipiscing elit. Nam tempor faucibus ante, eget vulputate libero pharetra eu. Nulla at.</p></div>
  <div class="product is-right" style="top:128px"><h3>Dwelling Fire</h3><p>Lorem ipsum dolor sit amet, consectetur adipiscing elit. Nam tempor faucibus ante, eget vulputate libero pharetra eu. Nulla at.</p></div>
  <div class="product is-left" style="top:304px"><h3>Renters/Condo</h3><p>Lorem ipsum dolor sit amet, consectetur adipiscing elit. Nam tempor faucibus ante, eget vulputate libero pharetra eu. Nulla at.</p></div>
  <div class="product is-right" style="top:304px"><h3>Agent Locator Tool</h3><p>Lorem ipsum dolor sit amet, consectetur adipiscing elit. Nam tempor faucibus ante, eget vulputate libero pharetra eu. Nulla at.</p></div>

  <div class="product-icon" style="left:452px;top:129px"><svg width="52" height="46" viewBox="0 0 52 46" fill="#fff"><path d="M26 3L2 23h7v20h12V31h10v12h12V23h7z"/></svg></div>
  <div class="product-icon" style="left:636px;top:129px"><svg width="54" height="48" viewBox="0 0 54 48" fill="#fff"><path d="M22 3L2 21h6v24h20V33c-3-2-4-6-2-10 2 3 4 2 4 0 0-4 3-8 7-10L22 3z"/><path d="M40 14c1 6 10 9 10 19 0 7-5 12-11 12s-10-4-10-10c0-5 3-7 5-9 0 3 1 5 3 5-1-7 2-12 3-17z"/><rect x="38" y="3" width="6" height="10"/></svg></div>
  <div class="product-icon" style="left:452px;top:310px"><svg width="52" height="44" viewBox="0 0 52 44" fill="#fff"><path d="M3 4h22v38H3z"/><path d="M28 16h21v26H28z"/><g fill="var(--navy-deep)"><rect x="7" y="9" width="5" height="5"/><rect x="16" y="9" width="5" height="5"/><rect x="7" y="18" width="5" height="5"/><rect x="16" y="18" width="5" height="5"/><rect x="7" y="27" width="5" height="5"/><rect x="16" y="27" width="5" height="5"/><rect x="32" y="21" width="5" height="5"/><rect x="41" y="21" width="5" height="5"/><rect x="32" y="30" width="5" height="5"/><rect x="41" y="30" width="5" height="5"/></g></svg></div>
  <div class="product-icon" style="left:636px;top:310px"><svg width="52" height="48" viewBox="0 0 52 48" fill="none" stroke="#fff" stroke-width="3"><path d="M6 4h28v38H6z"/><path d="M11 12h18M11 19h10M11 26h8M11 33h10"/><circle cx="32" cy="28" r="9" fill="var(--navy-deep)"/><path d="M38 35l9 9"/></svg></div>
</section>

<h2 class="blog-title">Latest <span class="accent">Blog</span></h2>
<article class="blog-card" style="left:78px"><h4>Blog Title</h4><p>Lorem Ipsum is simply dummy text of the printing and typesetting industry.</p><div class="blog-meta"><span>by admin</span><span><svg width="13" height="13" viewBox="0 0 13 13" fill="#555"><path d="M1 3h11v9H1zM3 0h2v3H3zM8 0h2v3H8z"/></svg>12th April 2017</span></div></article>
<article class="blog-card" style="left:438px"><h4>Blog Title</h4><p>Lorem Ipsum is simply dummy text of the printing and typesetting industry.</p><div class="blog-meta"><span>by admin</span><span><svg width="13" height="13" viewBox="0 0 13 13" fill="#555"><path d="M1 3h11v9H1zM3 0h2v3H3zM8 0h2v3H8z"/></svg>12th April 2017</span></div></article>
<article class="blog-card" style="left:799px"><h4>Blog Title</h4><p>Lorem Ipsum is simply dummy text of the printing and typesetting industry.</p><div class="blog-meta"><span>by admin</span><span><svg width="13" height="13" viewBox="0 0 13 13" fill="#555"><path d="M1 3h11v9H1zM3 0h2v3H3zM8 0h2v3H8z"/></svg>12th April 2017</span></div></article>

<footer class="site-footer">
  <div class="footer-tabs">
    <span style="left:58px">contact info</span><span style="left:229px">send message</span><span style="left:430px">view map</span>
  </div>
  <div class="tab-rule" style="left:308px;width:188px;background:var(--red)"></div>
  <div class="tab-rule" style="left:496px;width:398px;background:#9a9a9a"></div>

  <div class="contact-ring" style="left:180px"><svg width="28" height="28" viewBox="0 0 24 24" fill="var(--red)"><path d="M6.6 10.8a15 15 0 006.6 6.6l2.2-2.2c.3-.3.7-.4 1-.2 1.1.4 2.3.6 3.6.6.6 0 1 .4 1 1V20c0 .6-.4 1-1 1A17 17 0 013 4c0-.6.4-1 1-1h3.5c.6 0 1 .4 1 1 0 1.3.2 2.5.6 3.6.1.3 0 .7-.2 1z"/></svg></div>
  <div class="contact-ring" style="left:540px"><svg width="24" height="32" viewBox="0 0 24 32" fill="var(--red)"><path d="M12 0C5.4 0 0 5.4 0 12c0 9 12 20 12 20s12-11 12-20C24 5.4 18.6 0 12 0zm0 17a5 5 0 110-10 5 5 0 010 10z"/></svg></div>
  <div class="contact-ring" style="left:901px"><svg width="30" height="22" viewBox="0 0 30 22" fill="var(--red)"><path d="M0 0h30v3L15 12 0 3z"/><path d="M0 7l15 9 15-9v15H0z"/></svg></div>
  <div class="contact-dots" style="left:328px"></div>
  <div class="contact-dots" style="left:688px"></div>

  <p class="contact-text" style="left:140px;width:200px">123 456 7890</p>
  <p class="contact-text" style="left:430px;width:340px">Lorem Ipsum is simply dummy text of the printing and typesetting industry.</p>
  <p class="contact-text" style="left:831px;width:260px">info@hearthstead.com</p>

  <p class="copyright">©NORTHGATE FUND PARTNERS- 2018. All Rights Reserved. | Privacy policy | Terms and Conditions.</p>
</footer>

</body>
</html>
```